Consultant Firm Marketing Flyer

I want to use this flyer to market health care consultant services. I would like a front and back glossy, professional, yet bold and eye catching design. I would like it to convey knowledge, expertise, partnership and strength. The colors should blue and white but I am very open to the designer being creative. You can visit my website to see colors and images I want to use at brightmeadowadvisory.com
I would like the home page image on my website to be incorporated into the flyer but I am also open to other images that work with the design. The designer can be creative.

I want to highlight 4 service area’s of focus to my clients:
1. Revenue Cycle Optimization (making my clients money)
2. Practice Management Optimization (improving clinical operations)
3. Health Compliance (following the law)
4. Health Care Technology: (Telemedicine and AI)
Please be creative. Go where ever your creativity leads.

```html
<!DOCTYPE html>
<html lang="en">
<head>
<meta charset="utf-8">
<title>Bright Meadow Advisory – Advancing Healthcare Operations</title>
<link rel="stylesheet" href="https://fonts.googleapis.com/css2?family=Exo+2:wght@700;800&family=Saira:wght@400&display=swap">
<style>
  :root {
    --sky: #4ccfef;
    --royal: #1a5ff0;
    --deep: #1747d8;
    --disc: #f4f5f7;
    --ink: #1d1d1f;
    --photo-a: #c9ced6;
    --photo-b: #8a8f99;
  }
  html, body { margin: 0; padding: 0; overflow: hidden; background: #fff; }
  .flyer {
    position: relative; width: 927px; height: 1200px; overflow: hidden;
    background: #fff; font-family: "Saira", sans-serif; color: var(--ink);
  }
  .waves { position: absolute; inset: 0; }
  .headline {
    position: absolute; left: 40px; top: 50px; width: 320px; margin: 0;
    text-align: center; color: #fff; font-weight: 400; font-size: 33px; line-height: 38px;
  }
  .brand {
    position: absolute; font-family: "Exo 2", sans-serif; font-weight: 700;
    color: var(--royal); text-align: center; display: flex; align-items: center; gap: 8px;
  }
  .brand-mark { width: 14px; height: 14px; border-radius: 50%; background: var(--sky); flex: none; }
  .brand--top { left: 630px; top: 72px; font-size: 20px; }
  .brand--foot { left: 140px; top: 1100px; font-size: 22px; }
  .photo { position: absolute; background: linear-gradient(135deg, var(--photo-a), var(--photo-b)); }
  .photo--meeting { left: 639px; top: 184px; width: 288px; height: 180px; }
  .photo--desk { left: 0; top: 748px; width: 291px; height: 202px; background: linear-gradient(135deg, #d9dde2, #9a7c5e); }
  .service {
    position: absolute; width: 270px; height: 270px; border-radius: 50%;
    background: var(--disc); box-shadow: 4px 6px 10px rgba(0,0,0,.28);
    text-align: center; box-sizing: border-box;
  }
  .service h2 {
    margin: 0; font-family: "Exo 2", sans-serif; font-weight: 800;
    color: var(--sky); font-size: 15.5px; line-height: 20px; letter-spacing: .3px;
  }
  .service p { margin: 0 auto; font-size: 14.3px; line-height: 18.2px; }
  .service--revenue { left: 328px; top: 249px; padding: 54px 30px 0; }
  .service--compliance { left: 107px; top: 452px; padding: 50px 28px 0; }
  .service--hr { left: 557px; top: 452px; padding: 53px 26px 0; }
  .service--practice { left: 328px; top: 650px; padding: 52px 26px 0; }
  .badge {
    position: absolute; width: 106px; height: 106px; border-radius: 50%;
    background: var(--royal); display: flex; align-items: center; justify-content: center;
  }
  .badge svg { width: 66px; height: 66px; }
  .badge--revenue { left: 410px; top: 194px; }
  .badge--compliance { left: 189px; top: 396px; }
  .badge--hr { left: 639px; top: 374px; }
  .badge--practice { left: 410px; top: 597px; }
  .solutions-title {
    position: absolute; left: 367px; top: 533px; width: 200px; margin: 0; text-align: center;
    font-family: "Exo 2", sans-serif; font-weight: 800; font-size: 37px; color: var(--royal);
  }
  .contact-lead { position: absolute; left: 457px; top: 988px; margin: 0; font-size: 20px; }
  .contact { position: absolute; left: 457px; margin: 0; display: flex; align-items: center; gap: 22px;
    font-family: "Exo 2", sans-serif; font-weight: 800; color: var(--royal); }
  .contact svg { width: 24px; height: 24px; flex: none; }
  .contact--phone { top: 1030px; font-size: 27px; }
  .contact--mail { top: 1076px; font-size: 23px; }
  .contact--web { top: 1120px; font-size: 23px; }
</style>
</head>
<body>
<main class="flyer">
  <svg class="waves" viewBox="0 0 927 1200" width="927" height="1200" aria-hidden="true">
    <path d="M0,0 H543 C470,90 350,160 230,181 C140,194 60,180 0,158 Z" fill="var(--sky)"/>
    <path d="M560,150 C700,170 840,140 927,118 L927,132 C840,165 700,185 600,168 Z" fill="var(--sky)"/>
    <path d="M362,118 C460,155 570,170 680,163 C780,156 860,140 927,132 L927,140 C850,158 760,178 650,176 C520,172 420,150 362,118 Z" fill="var(--deep)"/>
    <g stroke="var(--sky)" stroke-width="16" stroke-linecap="butt">
      <line x1="300" y1="450" x2="340" y2="405"/>
      <line x1="600" y1="385" x2="645" y2="430"/>
      <line x1="290" y1="712" x2="345" y2="760"/>
      <line x1="640" y1="710" x2="598" y2="760"/>
    </g>
    <path d="M0,1200 L0,1108 C160,1010 360,935 560,930 C720,926 850,985 927,1035 L927,1048 C850,1005 720,962 560,967 C390,972 200,1060 70,1200 Z" fill="var(--deep)"/>
    <path d="M700,950 C800,965 870,1005 927,1035 L927,1048 C870,1015 800,985 700,975 Z" fill="var(--sky)"/>
  </svg>

  <h1 class="headline">Advancing Healthcare Operations</h1>
  <div class="brand brand--top"><span class="brand-mark"></span>Bright Meadow Advisory LLC</div>

  <div class="photo photo--meeting" role="img" aria-label="Photo of doctors and a consultant meeting around a table"></div>
  <div class="photo photo--desk" role="img" aria-label="Photo of two professionals reviewing work on a laptop"></div>

  <section class="service service--revenue">
    <h2>REVENUE CYCLE<br>MANAGEMENT</h2>
    <p>In today’s increasingly complex health care environment it’s important now more than ever that medical practices closely manage their revenue cycle. Bright Meadow Advisory (BMA) understands the reimbursement landscape</p>
  </section>
  <section class="service service--compliance">
    <h2>REGULATORY<br>COMPLIANCE</h2>
    <p>In a heavily regulated healthcare environment medical practices need to be acutely aware of regulations as they present huge liabilities. It is extremely important to ensure compliance with regulations. BMA offers a host of comprehensive compliance services.</p>
  </section>
  <section class="service service--hr">
    <h2>HUMAN RESOURCE<br>MANAGEMENT</h2>
    <p>Do you need Human Resources Management but don’t want the expense of a full service Human Resources Department? Not having a full service Human Resources Department can increase liability and be costly to your medical practice.</p>
  </section>
  <section class="service service--practice">
    <h2>PRACTICE<br>MANAGEMENT</h2>
    <p>Practice Management is challenging and it requires the right balance of skill, knowledge, experience and management expertise. BMA Offers assessment and optimization in Patient Access &amp; Scheduling, Patient Experience, Staff Experience</p>
  </section>

  <div class="badge badge--revenue">
    <svg viewBox="0 0 64 64" fill="none" stroke="var(--sky)" stroke-width="6">
      <path d="M14,26 A20,20 0 0 1 44,14"/><path d="M50,38 A20,20 0 0 1 20,50"/>
      <path d="M40,6 L48,15 L37,20" stroke-width="5"/><path d="M24,58 L16,49 L27,44" stroke-width="5"/>
    </svg>
  </div>
  <div class="badge badge--compliance">
    <svg viewBox="0 0 64 64">
      <path d="M12,6 H46 V54 H20 Q14,54 14,48 V14 Q14,8 10,8 Z" fill="var(--sky)"/>
      <path d="M20,54 H56 Q54,46 48,46 H22 Z" fill="var(--sky)"/>
      <path d="M30,18 L40,22 V30 Q40,38 30,42 Q20,38 20,30 V22 Z" fill="var(--royal)"/>
      <path d="M25,30 L29,34 L36,26" stroke="var(--sky)" stroke-width="3" fill="none"/>
    </svg>
  </div>
  <div class="badge badge--hr">
    <svg viewBox="0 0 64 64" fill="var(--sky)">
      <circle cx="34" cy="22" r="16"/>
      <circle cx="34" cy="22" r="10" fill="var(--royal)"/>
      <circle cx="34" cy="18" r="4"/><path d="M27,28 Q34,20 41,28 Z"/>
      <rect x="6" y="40" width="9" height="18"/>
      <path d="M18,42 H34 Q38,42 38,46 H28 L28,48 H44 L54,40 L58,44 L46,56 H18 Z"/>
    </svg>
  </div>
  <div class="badge badge--practice">
    <svg viewBox="0 0 64 64" fill="var(--sky)">
      <circle cx="32" cy="18" r="11"/><circle cx="32" cy="18" r="5" fill="var(--royal)"/>
      <path d="M6,20 L12,20 L14,38 L24,46 V58 H16 V50 L6,40 Z"/>
      <path d="M58,20 L52,20 L50,38 L40,46 V58 H48 V50 L58,40 Z"/>
    </svg>
  </div>

  <h2 class="solutions-title">Solutions</h2>

  <p class="contact-lead">Talk to a member of our team</p>
  <p class="contact contact--phone">
    <svg viewBox="0 0 24 24"><rect width="24" height="24" rx="4" fill="var(--royal)"/><path d="M7,5 L10,5 L11,9 L9,10 Q10,13 13,15 L14,13 L18,14 L18,17 Q17,19 15,19 Q6,17 5,8 Q5,6 7,5 Z" fill="#fff"/></svg>
    (555) 214-0190
  </p>
  <p class="contact contact--mail">
    <svg viewBox="0 0 24 24" fill="none" stroke="var(--royal)" stroke-width="2"><rect x="1" y="4" width="22" height="16" rx="2"/><path d="M1,5 L12,13 L23,5"/></svg>
    info@brightmeadowadvisory.com
  </p>
  <p class="contact contact--web">
    <svg viewBox="0 0 24 24"><circle cx="12" cy="12" r="11" fill="var(--royal)"/><path d="M6,7 Q10,5 12,8 Q10,11 8,11 Q8,15 6,14 Z M14,13 Q18,12 18,16 Q16,20 13,19 Z" fill="#fff"/></svg>
    www.brightmeadowadvisory.com
  </p>

  <div class="brand brand--foot"><span class="brand-mark"></span>Bright Meadow Advisory LLC</div>
</main>
</body>
</html>
```